New Coffee Shop business card

We are opening our new coffee shop and are needing business cards to take with us on February 6th to Atlanta, Ga to a show.

We will be offering the following menu type items:

coffee
teas
espresso
frappes
smoothies

sandwiches
soups
salads
pastries
ice cream

Our shop is in a rural country-side area and we would like to convey that feel in our shop. In addition to the cafe we will also be selling gifts and furniture and other home decor. Much of this merchandise will be rescued, refurbished or repurposed which is also a core value of what we are all about.

We have a company logo we would like incorporated into the design.

We will also provide files that have the elements of the logo which may also be useful in the design of the card.

Since we are not open yet we need one slightly altered version of the card as well as the final product which states "Opening in the summer 2015"

Target Market(s)

moderate to slightly upscale and folksy.

Industry/Entity Type

Coffee Shop

Contact Information for Business Card

Fern Hollow Coffee
name
address
phone number
email

Card

Font styles to use
Sans Serif

Requirements
Must have
• Must include Logo
• Must include information on menu.
• Must include information on our merchandise sales as described inthe project description.
• Color scheme to complement the logo
Nice to have
• The following descriptions
• "We are also selling gifts, furniture, and other home decoration."
• "We rescue, refurbish, and repurpose old furniture so it can live again."

```html
<!DOCTYPE html>
<html lang="en">
<head>
<meta charset="utf-8">
<title>Fern Hollow Coffee – Business Cards</title>
<link rel="stylesheet" href="https://fonts.googleapis.com/css2?family=Questrial&family=Open+Sans:wght@400;700&display=swap">
<style>
  :root {
    --backdrop: #3b302c;
    --paper: #f7f6f5;
    --ink: #2b2b2d;
    --maroon: #762c32;
    --charcoal: #2f2f31;
    --light: #ffffff;
    --ornament: #ebe6e3;
  }
  * { box-sizing: border-box; margin: 0; padding: 0; }
  html, body { width: 1200px; height: 768px; overflow: hidden; }
  body { background: var(--backdrop); position: relative; font-family: "Open Sans", sans-serif; color: var(--ink); }

  .card { position: absolute; width: 540px; height: 310px; background: var(--paper); overflow: hidden; box-shadow: 0 10px 30px rgba(0,0,0,.45); }
  .card--menu { left: 40px; top: 110px; }
  .card--contact { left: 620px; top: 340px; }

  .ornament { position: absolute; background: radial-gradient(ellipse at center, var(--ornament) 0%, rgba(235,230,227,0) 70%); }

  .brand { position: absolute; left: 34px; top: 36px; display: flex; align-items: center; gap: 12px; }
  .brand__dot { width: 22px; height: 22px; border-radius: 50%; background: var(--maroon); }
  .brand__name { font-family: "Questrial", sans-serif; font-size: 28px; line-height: 1.05; color: var(--ink); width: 170px; }

  .menu-list { position: absolute; left: 300px; top: 38px; list-style: none; font-family: "Questrial", sans-serif; font-size: 17px; line-height: 21px; }
  .menu-list li::before { content: "»"; color: var(--maroon); margin-right: 12px; }

  .band { position: absolute; bottom: 0; }
  .card--menu .band--maroon { left: 0; width: 330px; height: 30px; background: var(--maroon); }
  .card--menu .band--charcoal { left: 330px; right: 0; height: 30px; background: var(--charcoal); }

  .contact { position: absolute; left: 0; bottom: 0; width: 320px; height: 118px; background: var(--maroon); color: var(--light); padding: 16px 20px; font-size: 13px; line-height: 22px; }
  .contact__row { display: flex; align-items: center; gap: 8px; }
  .contact__row svg { width: 13px; height: 13px; fill: var(--light); flex: none; }
  .contact__sep { margin-left: 10px; }

  .menu-lines { position: absolute; right: 26px; top: 110px; text-align: right; font-size: 15px; line-height: 20px; }
  .menu-lines span { color: var(--maroon); }

  .person { position: absolute; right: 26px; top: 210px; text-align: right; }
  .person__name { font-weight: 700; font-size: 17px; }
  .person__title { font-size: 13px; }

  .website-bar { position: absolute; right: 0; bottom: 0; width: 220px; height: 36px; background: var(--charcoal); color: var(--light); font-size: 13px; display: flex; align-items: center; justify-content: flex-end; padding-right: 22px; }
</style>
</head>
<body>

  <section class="card card--menu" aria-label="Card front with menu">
    <div class="ornament" role="img" aria-label="Faint flourish and flying bird decoration" style="left:330px; top:20px; width:200px; height:250px;"></div>
    <div class="brand">
      <span class="brand__dot"></span>
      <span class="brand__name">Fern Hollow Coffee</span>
    </div>
    <ul class="menu-list">
      <li>Coffee</li><li>Teas</li><li>Espresso</li><li>Frappes</li><li>Smoothies</li>
      <li>Sandwiches</li><li>Soups</li><li>Salads</li><li>Pastries</li><li>Ice Cream</li>
    </ul>
    <div class="band band--maroon"></div>
    <div class="band band--charcoal"></div>
  </section>

  <section class="card card--contact" aria-label="Card back with contact details">
    <div class="ornament" role="img" aria-label="Faint flourish and flying bird decoration" style="left:320px; top:40px; width:210px; height:200px;"></div>
    <div class="brand" style="top:30px;">
      <span class="brand__dot"></span>
      <span class="brand__name">Fern Hollow Coffee</span>
    </div>

    <div class="contact">
      <div class="contact__row">
        <svg viewBox="0 0 16 16" aria-hidden="true"><path d="M3 1l3 3-2 2c1 2 4 5 6 6l2-2 3 3-2 2C7 15 1 9 1 3z"/></svg>
        <span>000 0 0 000 00</span>
        <svg class="contact__sep" viewBox="0 0 16 16" aria-hidden="true"><path d="M4 1h8v4H4zM1 6h14v7h-3v2H4v-2H1zM5 11v3h6v-3z"/></svg>
        <span>(03) 5550 0192</span>
      </div>
      <div class="contact__row">
        <svg viewBox="0 0 16 16" aria-hidden="true"><path d="M1 3h14v10H1zM2 4l6 5 6-5z" fill-rule="evenodd"/></svg>
        <span>hello@fernhollow.example</span>
      </div>
      <div class="contact__row">
        <svg viewBox="0 0 16 16" aria-hidden="true"><path d="M8 0a5 5 0 015 5c0 4-5 11-5 11S3 9 3 5a5 5 0 015-5zm0 3a2 2 0 100 4 2 2 0 000-4z"/></svg>
        <span>Your long commercial of office address</span>
      </div>
    </div>

    <div class="menu-lines">
      <p>Coffee <span>«</span> Teas <span>«</span></p>
      <p>Soups <span>«</span> Salads <span>«</span></p>
      <p>Espresso <span>«</span> Frappes <span>«</span></p>
      <p>Pastries <span>«</span> Ice Cream <span>«</span></p>
      <p>Smoothies <span>«</span> Sandwiches <span>«</span></p>
    </div>

    <div class="person">
      <p class="person__name">Your Long Name</p>
      <p class="person__title">Managing Director</p>
    </div>

    <div class="website-bar">www.fernhollow.example</div>
  </section>

</body>
</html>
```